Roofing Company Sales Rep Business Card

Business card for sales rep to canvass and hand out to property owners/managers for free roof inspections and roof replacements.

```html
<!DOCTYPE html>
<html lang="en">
<head>
<meta charset="utf-8">
<title>Ridgeline Roofing – Business Card</title>
<link href="https://fonts.googleapis.com/css2?family=Montserrat:wght@600;800&family=Open+Sans:wght@400&display=swap" rel="stylesheet">
<style>
  :root {
    --backdrop: #55585c;
    --card-white: #ffffff;
    --ink: #141414;
    --brand-red: #e01e25;
    --text-light: #ffffff;
  }
  html, body {
    margin: 0;
    width: 1200px;
    height: 887px;
    overflow: hidden;
    background: var(--backdrop);
  }
  .canvas {
    position: relative;
    width: 1200px;
    height: 887px;
  }
  .card {
    position: absolute;
    width: 600px;
    height: 343px;
    background: var(--card-white);
    border-radius: 26px;
    overflow: hidden;
    box-shadow: 0 14px 30px rgba(0,0,0,0.35);
  }
  .card--front { left: 90px; top: 60px; }
  .card--back  { left: 510px; top: 484px; }

  .brand {
    position: absolute;
    display: flex;
    align-items: center;
    gap: 12px;
    font-family: "Montserrat", sans-serif;
    font-weight: 800;
    color: var(--ink);
    letter-spacing: 0.02em;
    white-space: nowrap;
  }
  .brand__mark {
    background: var(--brand-red);
    flex: none;
  }
  .card--front .brand {
    left: 0; right: 0; top: 140px;
    justify-content: center;
    font-size: 40px;
  }
  .card--front .brand__mark { width: 30px; height: 30px; }
  .card--back .brand {
    left: 44px; top: 58px;
    font-size: 23px;
  }
  .card--back .brand__mark { width: 18px; height: 18px; }

  .wave {
    position: absolute;
    inset: 0;
    width: 600px;
    height: 343px;
  }

  .contact {
    position: absolute;
    right: 24px;
    top: 148px;
    text-align: right;
    color: var(--text-light);
    font-family: "Open Sans", sans-serif;
  }
  .contact__name {
    margin: 0;
    font-family: "Montserrat", sans-serif;
    font-weight: 800;
    font-size: 19px;
    line-height: 24px;
    color: var(--brand-red);
    letter-spacing: 0.02em;
  }
  .contact__role {
    margin: 0 0 8px;
    font-size: 13px;
  }
  .contact__list {
    list-style: none;
    margin: 0;
    padding: 0;
    font-size: 13px;
    line-height: 23px;
  }
  .contact__list li {
    display: flex;
    justify-content: flex-end;
    align-items: center;
    gap: 9px;
  }
  .contact__icon {
    width: 13px;
    height: 13px;
    fill: var(--brand-red);
    flex: none;
  }
</style>
</head>
<body>
<main class="canvas">

  <section class="card card--front" aria-label="Card front">
    <div class="brand"><span class="brand__mark"></span>RIDGELINE ROOFING</div>
  </section>

  <section class="card card--back" aria-label="Card back">
    <svg class="wave" viewBox="0 0 600 343" aria-hidden="true">
      <path d="M600,10 C470,14 430,60 380,150 C330,240 220,272 0,272" fill="none" stroke="var(--ink)" stroke-width="4" transform="translate(-12,-26)"/>
      <path d="M600,10 C470,14 430,60 380,150 C330,240 220,272 0,272 L0,343 L600,343 Z" fill="var(--brand-red)" transform="translate(-8,-15)"/>
      <path d="M600,10 C470,14 430,60 380,150 C330,240 220,272 0,272 L0,343 L600,343 Z" fill="var(--ink)" stroke="var(--card-white)" stroke-width="5" paint-order="stroke"/>
    </svg>

    <div class="brand"><span class="brand__mark"></span>RIDGELINE ROOFING</div>

    <div class="contact">
      <h1 class="contact__name">DANA WHITFIELD</h1>
      <p class="contact__role">Co-Founder</p>
      <ul class="contact__list">
        <li>555.014.2290
          <svg class="contact__icon" viewBox="0 0 24 24"><path d="M6.6 10.8a15 15 0 0 0 6.6 6.6l2.2-2.2c.3-.3.7-.4 1-.2 1.1.4 2.3.6 3.6.6.6 0 1 .4 1 1V20c0 .6-.4 1-1 1A17 17 0 0 1 3 4c0-.6.4-1 1-1h3.5c.6 0 1 .4 1 1 0 1.3.2 2.5.6 3.6.1.3 0 .7-.2 1z"/></svg>
        </li>
        <li>info@ridgeline-roof.com
          <svg class="contact__icon" viewBox="0 0 24 24"><path d="M2 5h20v14H2z M2 5l10 8 10-8" stroke="var(--ink)" stroke-width="1.5"/></svg>
        </li>
        <li>www.ridgeline-roof.com
          <svg class="contact__icon" viewBox="0 0 24 24"><circle cx="12" cy="12" r="10"/><path d="M2 12h20M12 2c3 3 3 17 0 20M12 2c-3 3-3 17 0 20" fill="none" stroke="var(--ink)" stroke-width="1.4"/></svg>
        </li>
        <li>42-07 Cedar Lane 14, Fairview
          <svg class="contact__icon" viewBox="0 0 24 24"><path d="M12 2a7 7 0 0 0-7 7c0 5 7 13 7 13s7-8 7-13a7 7 0 0 0-7-7zm0 9.5A2.5 2.5 0 1 1 12 6.5a2.5 2.5 0 0 1 0 5z"/></svg>
        </li>
      </ul>
    </div>
  </section>

</main>
</body>
</html>
```